Need a business cards for a hair dressing salon.

Target Market(s)

Target woman for Hair cuts, bridal makeup, occasion, fashion makeup and etc.

Industry/Entity Type

Hair

Font styles to use
Serif
Script

Requirements
Must have
• - Business card to be memorable and recognizable

- Please include the following on the business card:
- Business name: Salon Orimba
- Name: Kalini Desmodo (Name Must be changeable)
- Occupation: Hair Dresser & Beautician
- Contact number: 04 739 2 HAIR
- Email: mail@orimba.com.au
- Facebook (please use image): www.facebook.com/orimba.com.au
Nice to have
• Font Styles:
Business Name - Script
Other Text - Serif

```html
<!DOCTYPE html>
<html lang="en">
<head>
<meta charset="utf-8">
<title>Salon Orimba – Business Card</title>
<link rel="stylesheet" href="https://fonts.googleapis.com/css2?family=Playball&family=Crimson+Pro:wght@400;500&display=swap">
<style>
  :root {
    --page-bg: #ece9e6;
    --card-tint-cool: #cfe6ea;
    --card-tint-light: #eef0f0;
    --card-tint-warm: #f4ddd3;
    --brand: #b81f4e;
    --ink: #c42a4f;
  }
  * { box-sizing: border-box; margin: 0; padding: 0; }
  html, body {
    width: 1200px; height: 723px; overflow: hidden;
    background: var(--page-bg);
  }
  .card {
    position: absolute; left: 100px; top: 76px;
    width: 1000px; height: 571px;
    background: linear-gradient(155deg, var(--card-tint-cool) 0%, var(--card-tint-light) 45%, var(--card-tint-warm) 100%);
    box-shadow: 0 6px 24px rgba(0,0,0,.12);
  }
  .brand-name {
    position: absolute; left: 120px; top: 150px;
    font-family: "Playball", cursive;
    font-size: 120px; line-height: 1;
    color: var(--brand);
    white-space: nowrap;
  }
  .person { position: absolute; left: 270px; top: 330px; }
  .person-name {
    font-family: "Crimson Pro", serif;
    font-size: 44px; font-weight: 400;
    color: var(--ink); line-height: 1.1;
  }
  .person-role {
    font-family: "Crimson Pro", serif;
    font-size: 20px; font-weight: 500;
    letter-spacing: 1px; text-transform: uppercase;
    color: var(--ink); margin-top: 6px;
  }
  .contacts {
    position: absolute; left: 700px; top: 318px;
    list-style: none;
    font-family: "Crimson Pro", serif;
    font-size: 22px; color: var(--ink);
  }
  .contacts li { display: flex; align-items: center; gap: 10px; height: 34px; }
  .contacts svg { width: 18px; height: 18px; flex: none; }
</style>
</head>
<body>
  <div class="card">
    <div class="brand-name">Salon Orimba</div>

    <div class="person">
      <div class="person-name">Kalini Desmodo</div>
      <div class="person-role">Hair Dresser &amp; Beautician</div>
    </div>

    <ul class="contacts">
      <li>
        <svg viewBox="0 0 24 24" aria-hidden="true"><path d="M6.6 2.5l3 3.2-1.8 2.4c1.3 2.8 3.4 4.9 6.1 6.2l2.4-1.8 3.2 3-1.6 3.2C10.5 18.2 5.8 13.5 3.3 4.1z" fill="none" stroke="currentColor" stroke-width="1.8" stroke-linejoin="round"/></svg>
        <span>04 739 2 HAIR</span>
      </li>
      <li>
        <svg viewBox="0 0 24 24" aria-hidden="true"><circle cx="12" cy="12" r="4" fill="none" stroke="currentColor" stroke-width="2"/><path d="M16 12v1.5a2.5 2.5 0 0 0 5 0V12a9 9 0 1 0-3.5 7.1" fill="none" stroke="currentColor" stroke-width="2"/></svg>
        <span>mail@orimba.com.au</span>
      </li>
      <li>
        <svg viewBox="0 0 24 24" aria-hidden="true"><rect x="3" y="3" width="18" height="18" rx="2" fill="none" stroke="currentColor" stroke-width="2"/></svg>
        <span>/orimba.com.au</span>
      </li>
    </ul>
  </div>
</body>
</html>
```